Visitenkarten-Design für Programmierungen & Codierungen
Zielgruppe
Wir bieten Leistungssteigerungen Programmierungen & Codierungen für hochpreisige KfZ an. Unsere Kunden sind Geschäftsleute mit Teuren Autos und Feinsten Veredelungen.
Aufgabenstellung
Wir benötigen eine Visitenkarte in Schwarz mit Relieflack wo unser Firmenlogo hervorsticht, ich habe im Anhang ein Beispiel hinterlegt. Des weiteren soll die Visitenkarte im Querformat sein und Informationen wie Email Adresse, Telefonnummer, Fax, und Webadresse enthalten, nicht zu vergessen der Vor so wie der Nachname und Geschäftsführer. Das hochgeladene Firmenlogo soll auf der einen Seite stehen und auf der anderen kann ein Kleines von Ihnen erstellte Logo mit bspw. Karikatur oder ähnlichen neben den Kontaktinformationen stehen. Auch Leiterbahnen von einer Platine bspw. kann mit eingebracht werden.

```html
<!DOCTYPE html>
<html lang="de">
<head>
<meta charset="utf-8">
<title>Visitenkarte Voltrix Motorwerk</title>
<link href="https://fonts.googleapis.com/css2?family=Open+Sans:wght@400;600;700&display=swap" rel="stylesheet">
<style>
  :root {
    --backdrop: #121212;
    --card: #262627;
    --card-edge: #1c1c1d;
    --relief: #5a5a5c;
    --white: #f4f4f4;
    --red: #e3131b;
  }
  * { margin: 0; padding: 0; box-sizing: border-box; }
  html, body { width: 1200px; height: 912px; overflow: hidden; }
  body {
    background: var(--backdrop);
    font-family: "Open Sans", Arial, sans-serif;
    position: relative;
  }
  .card {
    position: absolute;
    width: 620px;
    height: 401px;
    background: linear-gradient(135deg, #2b2b2c 0%, var(--card) 55%, var(--card-edge) 100%);
    box-shadow: 0 18px 40px rgba(0,0,0,.6);
  }
  .card--back { left: 70px; top: 70px; }
  .card--front { left: 510px; top: 440px; overflow: hidden; }

  .brand {
    position: absolute;
    display: flex;
    align-items: center;
    gap: 12px;
    font-weight: 700;
    letter-spacing: 1px;
    text-transform: uppercase;
    white-space: nowrap;
  }
  .brand__mark { display: block; flex: none; }
  .card--back .brand {
    left: 50%; top: 50%;
    transform: translate(-50%, -50%);
    font-size: 40px;
    color: var(--relief);
  }
  .card--back .brand__mark {
    width: 34px; height: 34px;
    background: var(--relief);
  }
  .card--front .brand {
    left: 56px; top: 96px;
    font-size: 24px;
    color: var(--white);
  }
  .card--front .brand__mark {
    width: 24px; height: 24px;
    background: var(--red);
  }

  .person { position: absolute; right: 40px; top: 62px; }
  .person__name { color: var(--red); font-size: 18px; font-weight: 600; white-space: nowrap; }
  .person__role { color: var(--white); font-size: 13px; margin-top: 2px; margin-left: 18px; }

  .address {
    position: absolute; left: 56px; top: 200px;
    font-style: normal;
    color: var(--white); font-size: 15px; line-height: 22px;
  }
  .contacts {
    position: absolute; left: 56px; top: 262px;
    list-style: none;
    color: var(--white); font-size: 15px;
  }
  .contacts li { display: flex; align-items: center; gap: 12px; height: 23px; }
  .contacts svg { width: 15px; height: 15px; fill: var(--red); flex: none; }

  .accent-band {
    position: absolute; left: 0; right: 0; bottom: 0;
    height: 9px; background: var(--red);
  }
</style>
</head>
<body>

<section class="card card--back" aria-label="Rückseite">
  <div class="brand"><span class="brand__mark"></span>Voltrix Motorwerk</div>
</section>

<section class="card card--front" aria-label="Vorderseite">
  <div class="brand"><span class="brand__mark"></span>Voltrix Motorwerk</div>

  <div class="person">
    <div class="person__name">Lennart Falkenrath</div>
    <div class="person__role">Geschäftsführer</div>
  </div>

  <address class="address">
    Lindenweg 17<br>10785 Musterstadt
  </address>

  <ul class="contacts">
    <li>
      <svg viewBox="0 0 24 24"><path d="M6.6 10.8a15 15 0 0 0 6.6 6.6l2.2-2.2c.3-.3.7-.4 1-.2 1.1.4 2.3.6 3.6.6.6 0 1 .4 1 1V20c0 .6-.4 1-1 1A17 17 0 0 1 3 4c0-.6.4-1 1-1h3.5c.6 0 1 .4 1 1 0 1.3.2 2.5.6 3.6.1.3 0 .7-.2 1z"/></svg>
      02114 5093 210
    </li>
    <li>
      <svg viewBox="0 0 24 24"><path d="M7 3h10v5H7zM4 9h16a1 1 0 0 1 1 1v7h-4v4H7v-4H3v-7a1 1 0 0 1 1-1zm5 7v3h6v-3z"/></svg>
      02114 5093 211
    </li>
    <li>
      <svg viewBox="0 0 24 24"><path d="M2 5h20v14H2zm2 2v.5l8 5 8-5V7zm0 3v7h16v-7l-8 5z"/></svg>
      info@voltrix-motorwerk.de
    </li>
    <li>
      <svg viewBox="0 0 24 24"><path d="M12 2a10 10 0 1 0 0 20 10 10 0 0 0 0-20zm-1 17.9A8 8 0 0 1 4.2 10L9 14.8V16a2 2 0 0 0 2 2zm6.9-2.5A2 2 0 0 0 16 16h-1v-3a1 1 0 0 0-1-1H8v-2h2a1 1 0 0 0 1-1V7h2a2 2 0 0 0 2-2v-.4a8 8 0 0 1 2.9 12.8z"/></svg>
      www.voltrix-motorwerk.de
    </li>
  </ul>

  <div class="accent-band"></div>
</section>

</body>
</html>
```